Financial Advisor / Asset Manager Wix Design

I'm currently hosting with Wix and my first attempt at a website is live at www.bramwellhollowgroup.com Clearly I am not a web designer and I need help making this more catchy, modern, cross-platform compatible, search engine optimized, etc. I've got logos, hex color pallets, and a slew of other graphics. I'm interested in working with a winning designer to write/refine my copy/language to complete the build.

Full set of graphics https://albums.picnestly.io/r83Kd27WQfa5T1mZC do NOT use the CONSULTING graphics as this is for a related business / different website

Target Market(s)

Individuals, small institutions, endowments, non-profits seeking financial advice and asset / portfolio management

Industry/Entity Type

Financial Services

Coding

Coded - Design and coding required

Font styles to use
Other font styles liked:
• AvenirLTStd - Black, Book, and Roman as appropriate

Requirements
Must have
• Complete, cross platform website integrating my existing logo
Nice to have
• Easy to update format for go-forward maintenance

```html
<!DOCTYPE html>
<html lang="en">
<head>
<meta charset="utf-8">
<title>Bramwell Hollow Group — Personalized Financial Advice</title>
<link href="https://fonts.googleapis.com/css2?family=Nunito+Sans:wght@300;400;600;700;800;900&display=swap" rel="stylesheet">
<style>
:root{
  --blue:#1e80c6;
  --blue-deep:#135f9c;
  --navy:#0f2944;
  --navy-card:#112b48;
  --ink:#1d2733;
  --muted:#5b6673;
  --line:#dfe5ec;
  --paper:#ffffff;
  --mist:#f3f6f9;
}
*{box-sizing:border-box;margin:0;padding:0}
html,body{width:1200px;height:3472px;overflow:hidden}
body{font-family:"Nunito Sans",Arial,sans-serif;color:var(--ink);background:var(--paper);position:relative}
section,header,footer{position:absolute;left:0;width:1200px}
.btn{display:inline-block;font-size:15px;font-weight:600;padding:12px 30px;border-radius:2px;text-decoration:none}
.btn-white{background:#fff;color:var(--blue)}
.btn-blue{background:var(--blue);color:#fff}
.btn-outline{border:1px solid var(--blue);color:var(--blue);background:#fff}
.section-title{text-align:center;font-size:26px;font-weight:800;letter-spacing:1px;color:var(--ink)}
.section-title span{color:var(--blue)}

/* hero */
.hero{top:0;height:690px;overflow:hidden}
.hero-photo{position:absolute;inset:0;background:linear-gradient(180deg,#5f8fb8 0%,#8fb4d1 30%,#cfdde8 45%,#4f7590 60%,#2f5a76 80%,#4d7a96 100%)}
.hero-shade{position:absolute;inset:0;background:rgba(14,60,105,.28)}
.site-nav{position:absolute;top:0;left:0;width:1200px;height:100px;display:flex;align-items:center;justify-content:space-between;padding:0 160px}
.brand{color:#fff;font-weight:700;font-size:20px;letter-spacing:3px;display:flex;align-items:center;gap:12px}
.brand-dot{width:14px;height:14px;border-radius:50%;background:#fff}
.nav-links{display:flex;gap:40px;align-items:center}
.nav-links a{color:#fff;text-decoration:none;font-size:15px}
.nav-links a.nav-cta{border:1px solid #fff;padding:8px 26px}
.hero-copy{position:absolute;top:225px;width:1200px;text-align:center;color:#fff}
.hero-copy .light{font-size:42px;font-weight:300;line-height:1.12}
.hero-copy .bold{font-size:42px;font-weight:800;line-height:1.12}
.hero-copy .btn{margin-top:40px}
.hero-wave{position:absolute;bottom:0;left:0}

/* why */
.why{top:630px;height:370px}
.why-intro{width:640px;margin:22px auto 0;text-align:center;font-size:14px;line-height:1.6;color:var(--muted)}
.why-cards{display:flex;justify-content:center;align-items:center;gap:18px;margin-top:30px}
.why-card{width:150px;height:150px;background:#fff;box-shadow:0 4px 18px rgba(15,41,68,.12);display:flex;flex-direction:column;align-items:center;justify-content:flex-end;padding-bottom:18px;gap:22px;font-size:14px;font-weight:600}
.why-card.featured{width:190px;height:190px;background:var(--navy-card);color:#fff;justify-content:center;gap:10px;padding:18px}
.why-card.featured p{font-size:12px;font-weight:400;text-align:center;line-height:1.5;opacity:.85}
.why-card.featured strong{font-weight:600;color:#7fbfee}
.why-actions{display:flex;justify-content:center;gap:16px;margin-top:24px}

/* who */
.who{top:1010px;height:460px}
.who-band{position:absolute;inset:0;background:linear-gradient(180deg,var(--blue) 0%,var(--blue-deep) 100%);clip-path:polygon(0 8%,100% 0,100% 92%,0 100%)}
.who-text{position:absolute;left:160px;top:140px;width:400px;color:#fff}
.who-text h2{font-size:24px;font-weight:800;letter-spacing:1px;margin-bottom:20px}
.who-text p{font-size:14px;line-height:1.7;opacity:.92}
.who-photo{position:absolute;left:600px;top:85px;width:440px;height:260px;background:linear-gradient(135deg,#e9eef3 0%,#b8c6d3 45%,#54606c 100%);box-shadow:0 10px 30px rgba(0,0,0,.25)}

/* services */
.services{top:1500px;height:400px}
.service-cards{display:flex;justify-content:center;align-items:flex-start;gap:12px;margin-top:36px}
.service-card{width:232px;height:220px;background:#fff;box-shadow:0 4px 18px rgba(15,41,68,.12);padding:24px 22px;text-align:center}
.service-card.featured{background:var(--navy-card);color:#fff;height:240px}
.service-card h3{font-size:16px;font-weight:700;color:var(--blue);margin:12px 0 10px}
.service-card.featured h3{color:#7fbfee}
.service-card p{font-size:13px;line-height:1.6;color:var(--muted)}
.service-card.featured p{color:#d5e0ec}
.services .more{text-align:center;margin-top:30px}

/* inquiry */
.inquiry{top:1900px;height:340px}
.inquiry-band{position:absolute;inset:0;background:linear-gradient(135deg,#2b8fd3 0%,#1b74b8 55%,#155f98 100%);clip-path:polygon(0 0,100% 8%,100% 100%,0 92%)}
.inquiry h2{position:absolute;top:38px;width:1200px;text-align:center;color:#fff;font-size:22px;font-weight:800;letter-spacing:1px}
.inquiry-form{position:absolute;top:96px;left:380px;width:440px;display:grid;grid-template-columns:1fr 1fr;column-gap:20px;row-gap:16px}
.field{border-bottom:1px solid rgba(255,255,255,.6);color:#fff;font-size:12px;padding-bottom:8px;opacity:.9}
.field.wide{grid-column:1 / 3}
.inquiry .submit{position:absolute;top:250px;width:1200px;text-align:center}
.btn-ghost{border:1px solid #fff;color:#fff}

/* cta */
.cta{top:2250px;height:380px;overflow:hidden}
.cta-mountains{position:absolute;inset:0;background:linear-gradient(180deg,#ffffff 0%,#ffffff 40%,#eef2f6 70%,#dfe6ed 100%)}
.cta h2{position:relative;padding-top:62px;text-align:center;font-size:40px;font-weight:800;line-height:1.25;color:var(--ink)}
.cta h2 span{color:var(--blue)}
.cta .btn{position:relative;display:block;width:140px;margin:32px auto 0;text-align:center;padding:12px 0}

/* footer */
.site-footer{top:2630px;height:842px;background:#fff}
.footer-brand{position:absolute;left:160px;top:190px;width:320px;display:flex;flex-direction:column;align-items:center;gap:16px}
.footer-brand .mark{width:18px;height:18px;background:var(--navy)}
.footer-brand .name{font-size:28px;font-weight:700;letter-spacing:3px;color:var(--navy);text-align:center;line-height:1.25}
.footer-col{position:absolute;top:20px}
.footer-col h4{font-size:17px;font-weight:800;letter-spacing:.5px;margin-bottom:22px}
.footer-col h4 span{color:var(--blue)}
.quick-links{left:560px}
.quick-links a{display:block;font-size:14px;color:var(--ink);text-decoration:none;padding:9px 0 9px;border-bottom:1px solid var(--line);width:200px}
.contact-details{left:820px;width:240px}
.contact-item{display:flex;gap:12px;margin-bottom:22px}
.contact-item strong{display:block;font-size:14px;font-weight:700}
.contact-item span{font-size:13px;color:var(--muted);line-height:1.5}
.disclaimer{position:absolute;top:700px;left:160px;width:880px;background:var(--mist);padding:16px 30px;font-size:12px;line-height:1.6;color:var(--muted);text-align:center}
.bottom-bar{position:absolute;top:790px;left:0;width:1200px;height:52px;border-top:1px solid var(--line);display:flex;align-items:center;justify-content:space-between;padding:0 160px;font-size:12px;color:var(--muted)}
.follow{display:flex;align-items:center;gap:8px}
.follow i{width:14px;height:14px;background:var(--blue);display:inline-block}
</style>
</head>
<body>

<header class="hero">
  <div class="hero-photo" role="img" aria-label="Photograph of snow-capped mountains reflected in a still alpine lake"></div>
  <div class="hero-shade"></div>
  <nav class="site-nav">
    <div class="brand"><span class="brand-dot"></span>BRAMWELL HOLLOW GROUP</div>
    <div class="nav-links">
      <a href="#">Home</a><a href="#">About</a><a href="#">FAQs</a><a href="#">Services</a><a class="nav-cta" href="#">Contact</a>
    </div>
  </nav>
  <div class="hero-copy">
    <div class="light">Personalized Financial Advice</div>
    <div class="bold">To Help You Achieve Your Goals</div>
    <div class="light">Professional Management</div>
    <div class="bold">To Make Your Money Work For You</div>
    <a class="btn btn-white" href="#">Learn More</a>
  </div>
  <svg class="hero-wave" width="1200" height="90" viewBox="0 0 1200 90"><path d="M0 40 Q300 95 600 45 T1200 30 V90 H0Z" fill="#ffffff"/></svg>
</header>

<section class="why">
  <h2 class="section-title">WHY <span>CHOOSE US</span></h2>
  <p class="why-intro">Bramwell Hollow Group was founded with a purpose to make comprehensive and sophisticated financial services available to more investors. In addition to our unwavering commitment to our clients, we are dedicated to supporting and bettering our local communities.</p>
  <div class="why-cards">
    <div class="why-card">
      <svg width="44" height="44" viewBox="0 0 44 44" fill="none" stroke="#1e80c6" stroke-width="2"><circle cx="22" cy="14" r="7"/><path d="M8 38c2-9 8-13 14-13s12 4 14 13"/></svg>
      You Come First</div>
    <div class="why-card featured">
      <svg width="44" height="44" viewBox="0 0 44 44" fill="none" stroke="#7fbfee" stroke-width="2"><rect x="8" y="8" width="28" height="28" rx="3"/><path d="M15 22l5 5 10-11"/></svg>
      <strong>Personalized Services</strong>
      <p>We get to know you in order to service your unique needs.</p>
    </div>
    <div class="why-card">
      <svg width="44" height="44" viewBox="0 0 44 44" fill="none" stroke="#1e80c6" stroke-width="2"><rect x="9" y="6" width="26" height="32" rx="2"/><path d="M15 15h14M15 22h14M15 29h8"/></svg>
      Transparent Fees</div>
    <div class="why-card">
      <svg width="44" height="44" viewBox="0 0 44 44" fill="none" stroke="#1e80c6" stroke-width="2"><path d="M22 36S7 27 7 17a7.5 7.5 0 0 1 15-2 7.5 7.5 0 0 1 15 2c0 10-15 19-15 19z"/></svg>
      We Give Back</div>
  </div>
  <div class="why-actions"><a class="btn btn-blue" href="#">FAQs</a><a class="btn btn-outline" href="#">Contact Us</a></div>
</section>

<section class="who">
  <div class="who-band"></div>
  <div class="who-text">
    <h2>WHO WE ARE</h2>
    <p>Bramwell Hollow Group is an investment advisory firm committed to serving as fiduciary to our clients. We always act in the best interests of our clients, including putting your interests ahead of our own. We provide independent financial planning, investment management, and asset management services tailored to your unique needs and circumstances.</p>
  </div>
  <div class="who-photo" role="img" aria-label="Photograph of advisors reviewing financial charts on paper and a laptop"></div>
</section>

<section class="services">
  <h2 class="section-title">OUR <span>SERVICES</span></h2>
  <div class="service-cards">
    <div class="service-card">
      <svg width="40" height="40" viewBox="0 0 40 40" fill="none" stroke="#1e80c6" stroke-width="2"><rect x="6" y="8" width="28" height="26" rx="2"/><path d="M6 15h28M13 5v6M27 5v6"/></svg>
      <h3>Financial Planning</h3>
      <p>Lorem ipsum dolor sit amet, consectetuer adipiscing elit, sed diam nonummy nibh euismod tincidunt ut laoreet dolore magna aliquam.</p>
    </div>
    <div class="service-card featured">
      <svg width="40" height="40" viewBox="0 0 40 40" fill="none" stroke="#7fbfee" stroke-width="2"><path d="M6 34h28M10 30V20M18 30V12M26 30V16M34 30V8"/></svg>
      <h3>Asset Management</h3>
      <p>Many advisors use a screening process to find investments. You may be familiar with stock screening, or story websites that rank funds by past returns.</p>
    </div>
    <div class="service-card">
      <svg width="40" height="40" viewBox="0 0 40 40" fill="none" stroke="#1e80c6" stroke-width="2"><circle cx="20" cy="20" r="8"/><path d="M20 4v6M20 30v6M4 20h6M30 20h6"/></svg>
      <h3>Portfolio Optimization</h3>
      <p>Your investment portfolio was built with money you earned. It should be customized to reflect your goals and tailored to your plans.</p>
    </div>
    <div class="service-card">
      <svg width="40" height="40" viewBox="0 0 40 40" fill="none" stroke="#1e80c6" stroke-width="2"><circle cx="20" cy="20" r="14"/><path d="M20 6v14l10 6"/></svg>
      <h3>Alternative Investments</h3>
      <p>The challenges facing investors seeking to build portfolios capable of generating attractive returns with acceptable levels of risk.</p>
    </div>
  </div>
  <div class="more"><a class="btn btn-blue" href="#">Read More</a></div>
</section>

<section class="inquiry">
  <div class="inquiry-band"></div>
  <h2>QUICK INQUIRY</h2>
  <form class="inquiry-form">
    <div class="field">First Name</div><div class="field">Last Name</div>
    <div class="field wide">Email</div>
    <div class="field">ZIP Code</div><div class="field">Phone</div>
    <div class="field wide">Message</div>
  </form>
  <div class="submit"><a class="btn btn-ghost" href="#">Submit Now</a></div>
</section>

<section class="cta">
  <div class="cta-mountains" role="img" aria-label="Faint mountain range fading into white"></div>
  <h2>Come To Bramwell Hollow Group And<br><span>Find Out How We Can Do Better Together</span></h2>
  <a class="btn btn-blue" href="#">Contact Us</a>
</section>

<footer class="site-footer">
  <div class="footer-brand"><span class="mark"></span><div class="name">BRAMWELL<br>HOLLOW GROUP</div></div>
  <div class="footer-col quick-links">
    <h4>QUICK <span>LINKS</span></h4>
    <a href="#">Home</a><a href="#">About</a><a href="#">FAQs</a><a href="#">Services</a><a href="#">Contact</a>
  </div>
  <div class="footer-col contact-details">
    <h4>CONTACT <span>DETAILS</span></h4>
    <div class="contact-item">
      <svg width="18" height="18" viewBox="0 0 18 18" fill="#1e80c6"><path d="M9 1a6 6 0 0 0-6 6c0 4.5 6 10 6 10s6-5.5 6-10a6 6 0 0 0-6-6zm0 8.2A2.2 2.2 0 1 1 9 4.8a2.2 2.2 0 0 1 0 4.4z"/></svg>
      <div><span>2140 Larkspur Rd, Suite 310<br>Fernhill, VA 22910</span></div>
    </div>
    <div class="contact-item">
      <svg width="18" height="18" viewBox="0 0 18 18" fill="#1e80c6"><path d="M4 1l3 4-2 2c1 2 3 4 5 5l2-2 4 3-2 3C8 16 2 10 1 4z"/></svg>
      <div><strong>Phone</strong><span>+1 (434) 555-0147</span></div>
    </div>
    <div class="contact-item">
      <svg width="18" height="18" viewBox="0 0 18 18" fill="none" stroke="#1e80c6" stroke-width="1.6"><rect x="1.5" y="3.5" width="15" height="11"/><path d="M1.5 4l7.5 6 7.5-6"/></svg>
      <div><strong>Email</strong><span>info@bramwellhollowgroup.com</span></div>
    </div>
  </div>
  <p class="disclaimer">Bramwell Hollow Group LLC is a Registered Investment Advisor. We proudly serve as fiduciary to our clients and support our local communities. Past performance does not guarantee future results and all investing involves risk.</p>
  <div class="bottom-bar">
    <span>© 2022 BRAMWELL HOLLOW GROUP. All Rights Reserved.</span>
    <span class="follow">Follow Us On <i></i></span>
  </div>
</footer>

</body>
</html>
```